QX Community Page regarding All things QX Chatterline Chatbots, requires Profile and Banner images.

Hi, I have setup a QX Page for Reviews and News for all things related to Pallowtree Chatterline Chatbots. See https://www.pallowtree.example/chatterbotkits

I plan to post regular updates on new QX Chatterline Chatbots released and also on News regarding developments with Pallowtree Chatterline and also 3rd party platforms used to build Pallowtree Chatterline Chatbots. I am solely focussing on Pallowtree Chatterline Chatbots.

I hope to attract a huge community of like minded people interested in discussing use cases for Chatbots and recommendations of awesome QX Chatterline Chatbots.

Here is a similar idea for ALL Chatbots https://www.pallowtree.example/pg/droidrollco

I have attached my business Logo with colours. I don't intend for there to be a direct association but could probably hint an association by matching some colours. This is not important though as there is no direct connection. It is probably more important that Pallowtree Chatterline is the signal users will get when viewing the Page.

Target Market(s)

Pallowtree / Chatterline Users

Industry/Entity Type

Community

Requirements
Must have
• My website will look very similar to this one. I have bought this and it is in the process of being moved to my host and url. http://mind-forgery.example/
• the banner colour should match #0E94F9
Nice to have
• Would be nice if the font can match or be similar to the font used here http://mind-forgery.example/

```html
<!DOCTYPE html>
<html lang="en">
<head>
<meta charset="utf-8">
<title>QX Chatterline Community – Page Header</title>
<link rel="stylesheet" href="https://fonts.googleapis.com/css2?family=Open+Sans:wght@300&family=Source+Sans+3:wght@400;600&display=swap">
<style>
  :root {
    --page-bg: #ffffff;
    --banner-top: #27a7e1;
    --banner-mid: #1b76c6;
    --banner-dark: #252629;
    --accent: #0e94f9;
    --dot-mid: #1f7fb8;
    --dot-dim: #22445e;
    --frame-white: #ffffff;
    --avatar-bg: #242326;
    --bar-line: #dddfe2;
    --tab-text: #3d4247;
    --tab-active: #4b67a1;
    --headline: #ffffff;
  }
  * { margin: 0; padding: 0; box-sizing: border-box; }
  html, body { width: 1200px; height: 1200px; overflow: hidden; background: var(--page-bg); }
  .canvas { position: relative; width: 1200px; height: 1200px; }

  .page-header {
    position: absolute; left: 28px; top: 372px; width: 1144px; height: 481px;
    border: 1px solid var(--bar-line); border-top: none; background: #fff;
  }
  .cover {
    position: absolute; left: 0; top: 0; width: 100%; height: 420px;
    background: linear-gradient(180deg, var(--banner-top) 0%, #2189d4 28%, var(--banner-mid) 46%, #1f3e63 64%, var(--banner-dark) 80%, var(--banner-dark) 100%);
  }
  .network-art {
    position: absolute; left: 682px; top: 5px; width: 462px; height: 395px;
    background: radial-gradient(ellipse at 70% 30%, rgba(64, 232, 255, 0.28) 0%, rgba(40, 160, 230, 0.14) 45%, rgba(40, 120, 200, 0) 75%);
  }
  .tagline {
    position: absolute; left: 0; top: 123px; width: 100%; text-align: center;
    padding-right: 0; color: var(--headline);
  }
  .tagline svg { position: absolute; left: 448px; top: 0; }
  .tagline-text {
    position: absolute; left: 370px; top: 40px; width: 246px; text-align: center;
    font-family: 'Open Sans', sans-serif; font-weight: 300; font-size: 45px;
    letter-spacing: 0.5px; word-spacing: 6px; white-space: nowrap;
  }

  .avatar {
    position: absolute; left: 22px; top: 235px; width: 227px; height: 227px;
    background: var(--frame-white); border: 1px solid var(--bar-line);
    box-shadow: 0 1px 3px rgba(0,0,0,0.15); padding: 6px;
  }
  .avatar-inner {
    position: relative; width: 100%; height: 100%;
    background: radial-gradient(circle at 50% 36%, #46423f 0%, var(--avatar-bg) 45%);
  }
  .brand-name {
    position: absolute; left: 0; top: 66px; width: 100%; text-align: center;
    font-family: 'Source Sans 3', sans-serif; font-weight: 600; font-size: 30px;
    color: var(--accent);
  }
  .avatar-inner svg { position: absolute; left: 24px; top: 158px; }

  .tabs {
    position: absolute; left: 265px; top: 420px; height: 61px; display: flex;
    align-items: center; list-style: none;
    font-family: 'Source Sans 3', sans-serif; font-weight: 600; font-size: 18px; color: var(--tab-text);
  }
  .tab { position: relative; padding: 0 23px; height: 40px; line-height: 40px; }
  .tab + .tab { border-left: 1px solid var(--bar-line); }
  .tab.is-active::after {
    content: ""; position: absolute; left: 0; right: 0; bottom: -14px; height: 5px; background: var(--tab-active);
  }
</style>
</head>
<body>
<div class="canvas">
  <section class="page-header">
    <div class="cover">
      <div class="network-art" role="img" aria-label="Glowing network of connected nodes and lines"></div>
      <div class="tagline">
        <svg width="173" height="43" viewBox="0 0 173 43" aria-hidden="true">
          <path d="M14 1 H157 A15 15 0 0 1 157 41 H13 L1 43 Q5 38 5 32 V10 A9 9 0 0 1 14 1 Z" fill="none" stroke="#ffffff" stroke-width="1.3"/>
          <circle cx="21" cy="19" r="7" fill="#12a8f5"/>
          <circle cx="49" cy="19" r="7" fill="#1996dc"/>
          <circle cx="79" cy="19" r="7" fill="#1c7fc4"/>
        </svg>
        <p class="tagline-text">Bot is typing</p>
      </div>
    </div>

    <div class="avatar">
      <div class="avatar-inner">
        <p class="brand-name">Chatterline</p>
        <svg width="172" height="38" viewBox="0 0 172 38" aria-hidden="true">
          <rect x="0.7" y="0.7" width="170.6" height="36.6" rx="18.3" fill="none" stroke="#d8d8d8" stroke-width="1.2"/>
          <circle cx="21" cy="19" r="7.5" fill="#12a8f5"/>
          <circle cx="50" cy="19" r="7.5" fill="var(--dot-mid)"/>
          <circle cx="79" cy="19" r="7.5" fill="var(--dot-dim)"/>
        </svg>
      </div>
    </div>

    <ul class="tabs">
      <li class="tab is-active">Timeline</li>
      <li class="tab">About</li>
      <li class="tab">Photos</li>
      <li class="tab">Likes</li>
      <li class="tab">More</li>
    </ul>
  </section>
</div>
</body>
</html>
```